Dietitian needs a new business card design

I need a new business card design for my nutrition business that provides individual clinical nutrition advice for people with medical conditions. Business cards will be handed out to doctors, specialists and clients so will need to be sharp and project an image of professionalism

Target Market(s)

My clients are typically referred by doctors or specialists and the card will be used to handout to clients and their doctors.

Industry/Entity Type

Medical

Contact Information for Business Card

The business card will require the details below. These details can be found from my website https://www.kelvarrowclinic.com.au/

Font styles to use
Serif

Colors

Designer to choose colors to be used in the design.

Requirements
Must have
• 1. It needs be professional and contemporary
• 2. It needs to incorporate my logo
• 3. It needs space to write appointment times and dates
• 4. It needs to provide my phone number, fax number, email address and my web address
Nice to have
• Include the Registered Tovance Clinician Logo
• I have access to Framellow if required
• The locations I practise from
Should not have
• Pictures of food
• Spelling MIstakes

```html
<!DOCTYPE html>
<html lang="en">
<head>
<meta charset="utf-8">
<title>Kelvarrow Nutrition &amp; Dietetics – Business Card</title>
<link href="https://fonts.googleapis.com/css2?family=PT+Serif:wght@400;700&display=swap" rel="stylesheet">
<style>
  :root {
    --backdrop: #2b2e33;
    --card: #ffffff;
    --brand-blue: #1f5fae;
    --band-navy: #2c37a3;
    --brand-green: #69b23c;
    --rule-dash: #5b86c4;
    --edge: #d9dde3;
  }
  * { box-sizing: border-box; margin: 0; padding: 0; }
  html, body { width: 1200px; height: 900px; overflow: hidden; }
  body {
    background: var(--backdrop);
    font-family: "PT Serif", Georgia, serif;
    display: flex;
    align-items: center;
    justify-content: center;
    gap: 40px;
  }
  .card {
    position: relative;
    width: 540px;
    height: 310px;
    background: var(--card);
    border-radius: 24px;
    overflow: hidden;
    box-shadow: 0 0 0 1px var(--edge), 0 18px 40px rgba(0,0,0,.45);
  }

  /* Brand lockup */
  .brand { display: flex; align-items: center; gap: 10px; }
  .brand-dot { width: 34px; height: 34px; border-radius: 50%; flex: none; }
  .brand-name { line-height: 1; font-weight: 400; }
  .brand-name .word { display: block; font-size: 30px; }
  .brand-name .descriptor { display: block; font-size: 13px; margin-top: 3px; }

  /* Front */
  .card-front .brand { position: absolute; left: 30px; top: 28px; color: var(--brand-blue); }
  .card-front .brand-dot { background: var(--brand-green); }
  .divider { position: absolute; top: 158px; left: 30px; right: 30px; height: 4px; display: flex; }
  .divider .seg-blue { flex: 1; background: linear-gradient(90deg, #1c4fa6, #2f7fcc); }
  .divider .seg-green { flex: 1; background: var(--brand-green); margin-left: 4px; }
  .holder-name { position: absolute; right: 30px; top: 108px; font-size: 36px; color: var(--brand-blue); line-height: 1; }
  .holder-name .accent { color: var(--brand-green); }
  .holder-title { position: absolute; right: 30px; top: 172px; font-size: 17px; color: var(--brand-blue); }
  .holder-address { position: absolute; right: 30px; top: 212px; font-size: 16px; color: var(--brand-blue); text-align: right; line-height: 1.35; }
  .contact-list { position: absolute; left: 30px; top: 184px; list-style: none; color: var(--brand-blue); font-size: 15px; }
  .contact-list li { display: flex; align-items: center; gap: 8px; height: 26px; }
  .contact-list svg { width: 16px; height: 16px; flex: none; }

  /* Back */
  .band { position: absolute; inset: 0 0 auto 0; height: 92px; background: var(--band-navy); }
  .card-back .brand { position: absolute; right: 40px; top: 18px; color: #ffffff; }
  .card-back .brand-dot { background: #ffffff; }
  .appointment { position: absolute; left: 30px; right: 30px; top: 108px; color: var(--brand-blue); }
  .field { display: flex; align-items: flex-end; font-size: 15px; letter-spacing: .04em; }
  .field .line { flex: 1; border-bottom: 1px dashed var(--rule-dash); margin: 0 4px 4px; height: 1px; }
  .appointment-heading { text-align: center; font-size: 19px; letter-spacing: .12em; margin: 6px 0 12px 60px; }
  .days { display: flex; justify-content: space-between; font-size: 17px; letter-spacing: .04em; margin-bottom: 18px; }
  .day { display: flex; align-items: center; gap: 4px; }
  .day::before { content: ""; width: 13px; height: 13px; border: 1.5px solid var(--brand-blue); border-radius: 50%; }
</style>
</head>
<body>

  <section class="card card-front" aria-label="Business card front">
    <div class="brand">
      <span class="brand-dot"></span>
      <span class="brand-name"><span class="word">Kelvarrow</span><span class="descriptor">Nutrition &amp; Dietetics</span></span>
    </div>

    <p class="holder-name">Your <span class="accent">Name</span></p>
    <div class="divider"><span class="seg-blue"></span><span class="seg-green"></span></div>
    <p class="holder-title">Your Title</p>
    <p class="holder-address">Your Address, City<br>State, Zip 0000, Country</p>

    <ul class="contact-list">
      <li>
        <svg viewBox="0 0 16 16" aria-hidden="true"><circle cx="8" cy="8" r="8" fill="#69b23c"/><path d="M5.4 4.2l1.3-.2.7 1.8-.9.7c.4.9 1.1 1.6 2 2l.7-.9 1.8.7-.2 1.3c-.1.5-.6.8-1.1.7-2.6-.5-4.4-2.3-4.9-4.9-.1-.6.2-1.1.6-1.2z" fill="#fff"/></svg>
        0123456789
      </li>
      <li>
        <svg viewBox="0 0 16 16" aria-hidden="true"><circle cx="8" cy="8" r="8" fill="#69b23c"/><rect x="4" y="5.2" width="8" height="5.6" rx=".6" fill="#fff"/><path d="M4.3 5.6L8 8.4l3.7-2.8" stroke="#69b23c" stroke-width=".9" fill="none"/></svg>
        hello@kelvarrowclinic.com.au
      </li>
      <li>
        <svg viewBox="0 0 16 16" aria-hidden="true"><circle cx="8" cy="8" r="8" fill="#69b23c"/><circle cx="8" cy="8" r="4" fill="none" stroke="#fff" stroke-width="1"/><ellipse cx="8" cy="8" rx="1.7" ry="4" fill="none" stroke="#fff" stroke-width=".9"/><path d="M4 8h8" stroke="#fff" stroke-width=".9"/></svg>
        www.kelvarrowclinic.com.au
      </li>
    </ul>
  </section>

  <section class="card card-back" aria-label="Business card back, appointment card">
    <div class="band"></div>
    <div class="brand">
      <span class="brand-dot"></span>
      <span class="brand-name"><span class="word">Kelvarrow</span><span class="descriptor">Nutrition &amp; Dietetics</span></span>
    </div>

    <div class="appointment">
      <div class="field">FOR<span class="line"></span></div>
      <p class="appointment-heading">APPOINTMENT</p>
      <div class="days">
        <span class="day">MON</span><span class="day">TUE</span><span class="day">WED</span>
        <span class="day">THU</span><span class="day">FRI</span><span class="day">SAT</span>
      </div>
      <div class="field">DATE<span class="line"></span>TIME<span class="line"></span>AM/PM</div>
    </div>
  </section>

</body>
</html>
```